Supper Among Giants Private Fundraising Experience

We need to create a brand identity for exclusive private corporate fundraising events titled "Supper Among Giants". The concept is to merge the Chicago corporate community with local celebrated Chefs to create a unique dining experience in conjunction with a fundraiser benefiting the Reid Hollister Foundation..www.reidhollisterfund-example.org
These events will take place throughout the year. They will be limited to 50 people to maintain an intimate and exclusive atmoshpere.
We need marketing collateral design for a flyer and an electronic version of the flyer for our website and other use. The design should communicate a sense of exclusivity, and an opportunity to dine privately with some of the greatest sports legends and help support the Reid Hollister Foundations mission of investing in schools whose primary goal is to better prepare students for college and or a career through the effective use of classroom technology. We would like to create a marketing campaign and brand identity for these series of smaller private exclusive corporate or individual sponsored fundraising events.

Target Market(s)

Corporations and Individuals who would pay to have a unique dining experience and help support a local fundraising cause (Reid Hollister Foundation)

Industry/Entity Type

Non Profit

Number of Pages Required

2 page

Font styles to use
Script
Other font styles liked:
• Bikram

Requirements
Must have
• Our logo, high res, high impact, high quality images and graphic design. Images of celebrity chefs and sports legends. High impact people, food, and table setting images.
• Images of famous american athletes including one of Reid Hollister.
• I would use an image of a famous player from every major U.S, sport, football, = Reid Hollister, basketball, baseball, and hockey.
• This should be a double sides flyer so that we can utilize more images and content.

```html
<!DOCTYPE html>
<html lang="en">
<head>
<meta charset="utf-8">
<title>Supper Among Giants</title>
<link href="https://fonts.googleapis.com/css2?family=Open+Sans:wght@400;600;700;800&display=swap" rel="stylesheet">
<style>
:root{
  --blue:#1a5fb4;
  --blue-deep:#0d3f82;
  --blue-bright:#2b86e0;
  --orange:#f7941d;
  --ink:#2a2f36;
  --muted:#6b7280;
  --grey:#e6e7e9;
  --dark:#2b2d30;
  --white:#ffffff;
}
*{box-sizing:border-box;margin:0;padding:0}
html,body{width:1200px;height:3156px;overflow:hidden}
body{font-family:'Open Sans',Arial,sans-serif;color:var(--ink);background:var(--white);position:relative}
.abs{position:absolute}
.photo{position:absolute;display:block}

/* header & hero */
.hero{left:0;top:0;width:1200px;height:580px;background:linear-gradient(165deg,#3a2c24 0%,#5c4738 35%,#8a7464 65%,#2c2420 100%)}
.brand{left:40px;top:42px;display:flex;align-items:center;gap:10px;font-weight:800;font-size:19px;line-height:23px;color:var(--blue);letter-spacing:.4px}
.brand .dot{width:12px;height:12px;background:var(--orange);border-radius:50%;flex:none}
.brand .name span{display:block;white-space:nowrap}
.phone-btn{left:900px;top:0;width:210px;height:34px;background:var(--blue-bright);color:var(--white);font-size:13px;font-weight:700;display:flex;align-items:center;justify-content:center;gap:8px;border-radius:0 0 6px 6px}
.nav{left:520px;top:56px;display:flex;gap:14px}
.nav a{display:block;width:86px;height:28px;line-height:28px;text-align:center;font-size:10.5px;font-weight:700;color:var(--blue);background:var(--white);border-radius:4px;text-decoration:none;white-space:nowrap}
.nav a.active{background:var(--blue-bright);color:var(--white)}
.hero-copy{left:0;width:1200px;top:292px;text-align:center;color:var(--white);font-weight:700;font-size:19px;line-height:44px;text-shadow:0 1px 3px rgba(0,0,0,.5)}

/* welcome */
.welcome{left:0;top:580px;width:1200px;height:460px}
.welcome-title{left:0;width:1200px;top:606px;text-align:center;color:var(--white)}
.welcome-title .small{font-size:21px;font-weight:700;letter-spacing:1px;line-height:28px}
.welcome-title .big{font-size:30px;font-weight:800;letter-spacing:1px;line-height:38px;margin-top:4px}
.welcome-img{left:160px;top:720px;width:256px;height:250px;background:linear-gradient(135deg,#c9d2dc,#5d6670);border:4px solid var(--white)}
.welcome-text{left:488px;top:722px;width:592px;color:#dbe8fa;font-size:13px;line-height:19px}
.btn-more{left:488px;top:940px;width:96px;height:30px;background:var(--blue-bright);color:var(--white);font-size:11px;font-weight:700;display:flex;align-items:center;justify-content:center;border-radius:3px}

/* section titles */
.sec-title{left:0;width:1200px;text-align:center;font-size:22px;line-height:30px;font-weight:700;color:var(--ink)}
.sec-title em{font-style:normal;color:var(--blue-bright);border-bottom:3px solid var(--orange)}

/* gallery */
.gallery-panel{left:160px;top:1172px;width:888px;height:420px;background:var(--grey)}
.g{width:268px;height:180px}

/* events */
.events-bg{left:0;top:1640px;width:1200px;height:840px}
.event{position:absolute;width:440px;height:250px}
.event .pic{position:absolute;left:0;top:10px;width:192px;height:240px;border-radius:6px}
.event .tag{position:absolute;left:98px;top:0;width:82px;height:60px;background:var(--blue-bright);color:var(--white);font-weight:800;font-size:20px;line-height:24px;text-align:center;padding-top:6px}
.event .tag:after{content:"";position:absolute;right:-16px;top:0;border-left:16px solid var(--blue-bright);border-top:30px solid transparent;border-bottom:30px solid transparent}
.event h3{position:absolute;left:212px;top:10px;font-size:15px;line-height:20px;font-weight:600;color:var(--blue-bright);width:220px;white-space:nowrap}
.event p{position:absolute;left:212px;top:38px;width:215px;font-size:12px;line-height:17px;color:var(--muted)}

/* contact */
.contact-photo{left:0;top:2544px;width:1200px;height:376px;background:linear-gradient(120deg,#c9b7a2 0%,#7b8ea0 45%,#3f5a78 100%)}
.tablet{left:100px;top:2574px;width:600px;height:346px;background:#1f2326;border-radius:26px 26px 0 0}
.card{left:150px;top:2620px;width:500px;height:290px;background:var(--white)}
.card .brand{position:absolute;left:26px;top:22px;font-size:18px;line-height:22px}
.card p{position:absolute;font-size:12px;line-height:16px;color:var(--muted)}
.form{left:740px;top:2652px;width:300px}
.form .field{height:26px;background:rgba(30,32,36,.85);color:#c7ccd2;font-size:11px;padding-left:10px;line-height:26px;margin-bottom:8px}
.form .field.area{height:70px}
.form .send{width:70px;height:26px;background:var(--blue-bright);color:var(--white);font-size:11px;font-weight:700;display:flex;align-items:center;justify-content:center}

/* footer */
.footer{left:0;top:2920px;width:1200px;height:236px;background:var(--dark);color:#9aa0a6;text-align:center}
.socials{display:flex;justify-content:center;gap:10px;margin-top:36px}
.socials i{width:22px;height:22px;border-radius:50%;background:var(--blue-bright);display:block}
.footer p{font-size:12px;line-height:16px;margin-top:14px}
.footer .fine{font-size:10px;margin-top:6px;color:#7c8288}
</style>
</head>
<body>

<div class="photo hero" role="img" aria-label="Guests sharing a plated dinner at a restaurant table with a wine wall behind"></div>
<div class="abs brand"><span class="dot"></span><div class="name"><span>SUPPER AMONG</span><span>GIANTS</span></div></div>
<div class="abs phone-btn">
  <svg width="14" height="14" viewBox="0 0 24 24" fill="#fff"><path d="M6.6 10.8a15 15 0 0 0 6.6 6.6l2.2-2.2a1 1 0 0 1 1-.25 11.4 11.4 0 0 0 3.6.57 1 1 0 0 1 1 1V20a1 1 0 0 1-1 1A17 17 0 0 1 3 4a1 1 0 0 1 1-1h3.5a1 1 0 0 1 1 1c0 1.25.2 2.45.57 3.57a1 1 0 0 1-.25 1z"/></svg>
  +1 (312) 555 0148
</div>
<nav class="abs nav">
  <a class="active">HOME</a><a>ABOUT US</a><a>GALLERY</a><a>EVENTS</a><a>BLOG</a><a>CONTACT US</a>
</nav>
<div class="abs hero-copy">
  <div>Lorem ipsum dolor sit amet</div>
  <div>Amet consectetur Adipiscing dummy</div>
  <div>Lorem ipsum dolor sit amet</div>
</div>

<svg class="abs welcome" viewBox="0 0 1200 460" width="1200" height="460">
  <defs><linearGradient id="wg" x1="0" y1="0" x2="0" y2="1"><stop offset="0" stop-color="#1a5fb4"/><stop offset="1" stop-color="#0d3f82"/></linearGradient></defs>
  <polygon points="0,0 1200,0 1200,380 600,455 0,380" fill="url(#wg)"/>
</svg>
<div class="abs welcome-title"><div class="small">WEL COME TO</div><div class="big">SUPPER AMONG GIANTS</div></div>
<div class="photo welcome-img" role="img" aria-label="Speaker at a microphone during a fundraising dinner"></div>
<p class="abs welcome-text">Lorem ipsum dolor sit amet, consectetur adipiscing elit. Nunc pellentesque massa id eleifend malesuada. Fusce at imperdiet lorem. Morbi auctor auctor pretium. Nisi vel accumsan volutpat, nunc tortor semper velit, vel tincidunt ligula lorem eget nisi. Mauris placerat urna quis tempus commodo. Integer vitae facilisis lorem, sed pharetra nulla. Curabitur in tempor ipsum, id hendrerit enim. Donec ut lacus at erat ultricies aliquet. Vivamus dictum porta magna, quis feugiat quam finibus in. Praesent convallis sapien sed lectus viverra, vel sodales dui porta. Aenean mollis diam vitae turpis dignissim rutrum. Sed at lacus vitae nisl gravida tempor. Quisque vel mauris non nibh laoreet posuere. Nulla facilisi. Etiam aliquet velit at sem fringilla, in luctus risus iaculis. Phasellus ac tortor eu erat sagittis luctus sed non ante.</p>
<div class="abs btn-more">FIND MORE</div>

<h2 class="abs sec-title" style="top:1118px">LATEST <em>GALLERY</em></h2>
<div class="abs gallery-panel"></div>
<div class="photo g" style="left:176px;top:1190px;background:linear-gradient(135deg,#2d3f6a,#8b6e62)" role="img" aria-label="Group of guests posing together at an event"></div>
<div class="photo g" style="left:470px;top:1190px;background:linear-gradient(135deg,#e8e4dc,#b98a4e)" role="img" aria-label="Plated dish of roasted food"></div>
<div class="photo g" style="left:764px;top:1190px;background:linear-gradient(135deg,#a9c07a,#d6b89a)" role="img" aria-label="Couple smiling outdoors"></div>
<div class="photo g" style="left:176px;top:1390px;background:linear-gradient(135deg,#e08a1e,#c86d10)" role="img" aria-label="Orange textured backdrop"></div>
<div class="photo g" style="left:470px;top:1390px;background:linear-gradient(135deg,#3a3030,#a23030)" role="img" aria-label="Guests in formal wear at a gala"></div>
<div class="photo g" style="left:764px;top:1390px;background:linear-gradient(135deg,#2a3f8a,#b4533a)" role="img" aria-label="Sports memorabilia on display"></div>

<svg class="abs events-bg" viewBox="0 0 840 840" preserveAspectRatio="none" width="1200" height="840">
  <polygon points="0,0 420,30 840,0 840,780 420,840 0,780" fill="#e6e7e9"/>
</svg>
<h2 class="abs sec-title" style="top:1660px">LATEST <em>EVENTS</em></h2>

<div class="event" style="left:160px;top:1740px">
  <div class="pic" style="background:linear-gradient(135deg,#7a2a2a,#c9c1b4)" role="img" aria-label="Guest holding a framed jersey"></div>
  <div class="tag">OCT<br>2015</div>
  <h3>Lorem ipsum dolor sit</h3>
  <p>Lorem ipsum dolor sit amet, consectetur adipiscing elit. Nunc pellentesque massa id eleifend malesuada. Fusce at imperdiet lorem. Morbi auctor auctor pretium. Nisi vel accumsan.</p>
</div>
<div class="event" style="left:620px;top:1740px">
  <div class="pic" style="background:linear-gradient(135deg,#394a63,#8d7a6a)" role="img" aria-label="Crowd seated at a banquet"></div>
  <div class="tag">OCT<br>2015</div>
  <h3>Lorem ipsum dolor sit</h3>
  <p>Lorem ipsum dolor sit amet, consectetur adipiscing elit. Nunc pellentesque massa id eleifend malesuada. Fusce at imperdiet lorem. Morbi auctor auctor pretium. Nisi vel accumsan.</p>
</div>
<div class="event" style="left:160px;top:2048px">
  <div class="pic" style="background:linear-gradient(135deg,#4a3b55,#a98e7a)" role="img" aria-label="Two guests in suits at an event"></div>
  <div class="tag">OCT<br>2015</div>
  <h3>Lorem ipsum dolor sit</h3>
  <p>Lorem ipsum dolor sit amet, consectetur adipiscing elit. Nunc pellentesque massa id eleifend malesuada. Fusce at imperdiet lorem. Morbi auctor auctor pretium. Nisi vel accumsan.</p>
</div>
<div class="event" style="left:620px;top:2048px">
  <div class="pic" style="background:linear-gradient(135deg,#1e2a44,#5a6b86)" role="img" aria-label="Speaker addressing the audience"></div>
  <div class="tag">OCT<br>2015</div>
  <h3>Lorem ipsum dolor sit</h3>
  <p>Lorem ipsum dolor sit amet, consectetur adipiscing elit. Nunc pellentesque massa id eleifend malesuada. Fusce at imperdiet lorem. Morbi auctor auctor pretium. Nisi vel accumsan.</p>
</div>

<h2 class="abs sec-title" style="top:2500px">CONTACT <em>US</em></h2>
<div class="photo contact-photo" role="img" aria-label="City waterfront skyline seen behind a hand holding a tablet"></div>
<div class="abs tablet"></div>
<div class="abs card">
  <div class="brand"><span class="dot"></span><div class="name"><span>SUPPER AMONG</span><span>GIANTS</span></div></div>
  <p style="left:26px;top:84px;width:450px">Lorem ipsum dolor sit amet, consectetur adipiscing elit. Nunc pellentesque massa id eleifend malesuada. Fusce at imperdiet lorem. Morbi auctor auctor pretium. Nisi vel accumsan volutpat, nunc tortor semper velit, vel tincidunt ligula lorem eget nisi.</p>
  <p style="left:26px;top:190px">Name: Lorem Ipsum<br>City: Dummy<br>Code No: 0123456</p>
  <p style="left:250px;top:190px">Address: Dummy Address<br>Street: Lorem Ipsum</p>
</div>
<div class="abs form">
  <div class="field">Name</div>
  <div class="field">Email</div>
  <div class="field">Telephone</div>
  <div class="field">Mobile</div>
  <div class="field area">Comments</div>
  <div class="send">Submit</div>
</div>

<footer class="abs footer">
  <div class="socials"><i></i><i></i><i></i><i></i><i></i><i></i></div>
  <p>Copyright © 2015 Supper Among Giants. All rights reserved.</p>
  <p class="fine">Privacy Policy | Terms of Use | Sitemap | Contact</p>
</footer>

</body>
</html>
```